Korvex Global ltd. Stationaries
Full Stationary set
Korvex Global ltd. Stationaries  -
Creative Brief
Professional
Owen Pallister
VP, Sales MENA
Korvex Global Limited Zerhani Tower Office No. 614-616, 6th Floor Qasr Nadeem Road, Hessa P.O. Box 4827 Dubai, UAE
owen.pallister@korvexglb.example
korvexglb.example
All Size A4 (European Size) - Letterhead (Word Template, PDF, AI) - Purchase Order (Excel Template, PDF, AI) - Quotation (Excel Template, PDF, AI) - Invoice (Excel Template, PDF, AI) - Envelope (Big, Medium, Small) - Business Card (front and back) - Power Point Template - CD/DVD (label and jacket) - Folder
Broadcasting Solutions

```html
<!DOCTYPE html>
<html lang="en">
<head>
<meta charset="utf-8">
<title>Korvex Global ltd. – Business Card</title>
<link rel="stylesheet" href="https://fonts.googleapis.com/css2?family=Open+Sans:wght@400;600;700&family=Crimson+Pro:wght@400&display=swap">
<style>
  :root {
    --stage: #e4e5e7;
    --card: #ffffff;
    --ink: #3a3a3a;
    --ink-soft: #5a5a5a;
    --name-blue: #2b7cb9;
    --title-green: #4c9a3c;
    --divider: #cfcfcf;
    --band-light: #e9e9e9;
    --band-dark: #bdbdbd;
    --mark: #3d3d3d;
  }
  * { box-sizing: border-box; margin: 0; padding: 0; }
  html, body { width: 1200px; height: 780px; overflow: hidden; }
  body {
    background: var(--stage);
    display: flex;
    align-items: center;
    justify-content: center;
  }
  .business-card {
    position: relative;
    width: 840px;
    height: 480px;
    background: var(--card);
    border-radius: 34px;
    overflow: hidden;
    box-shadow: 0 10px 30px rgba(0,0,0,0.18);
  }
  .brand {
    position: absolute;
    left: 40px;
    top: 218px;
    width: 296px;
    display: flex;
    align-items: center;
    gap: 12px;
  }
  .brand-dot {
    flex: 0 0 40px;
    width: 40px;
    height: 40px;
    border-radius: 50%;
    background: var(--name-blue);
  }
  .brand-name {
    font-family: "Open Sans", sans-serif;
    font-weight: 700;
    font-size: 24px;
    color: var(--mark);
    line-height: 1.1;
    white-space: nowrap;
  }
  .divider {
    position: absolute;
    left: 358px;
    top: 36px;
    width: 1px;
    height: 400px;
    background: var(--divider);
  }
  .details {
    position: absolute;
    left: 386px;
    top: 34px;
    right: 30px;
  }
  .person-name {
    font-family: "Open Sans", sans-serif;
    font-weight: 700;
    font-size: 27px;
    color: var(--name-blue);
    line-height: 1.15;
  }
  .person-title {
    font-family: "Open Sans", sans-serif;
    font-weight: 600;
    font-size: 16px;
    color: var(--title-green);
    margin-top: 2px;
  }
  .address {
    font-family: "Crimson Pro", serif;
    font-style: normal;
    font-size: 21px;
    line-height: 25px;
    color: var(--ink);
    margin-top: 38px;
  }
  .contacts {
    list-style: none;
    margin-top: 24px;
    font-family: "Crimson Pro", serif;
    font-size: 21px;
    color: var(--ink);
  }
  .contacts li {
    display: flex;
    align-items: center;
    gap: 12px;
    height: 32px;
  }
  .contact-icon {
    width: 18px;
    height: 18px;
    display: inline-flex;
    align-items: center;
    justify-content: center;
    color: var(--ink-soft);
    font-family: "Open Sans", sans-serif;
    font-weight: 700;
    font-size: 18px;
  }
  .phone-icon { color: var(--name-blue); }
  .web-icon { color: var(--name-blue); }
  .footer-band {
    position: absolute;
    right: 0;
    bottom: 0;
    width: 360px;
    height: 44px;
    background: linear-gradient(90deg, var(--band-light), var(--band-dark));
    clip-path: polygon(40px 0, 100% 0, 100% 100%, 0 100%);
  }
</style>
</head>
<body>
  <article class="business-card">
    <div class="brand">
      <span class="brand-dot"></span>
      <span class="brand-name">Korvex Global ltd.</span>
    </div>

    <div class="divider"></div>

    <section class="details">
      <h1 class="person-name">Owen Pallister</h1>
      <p class="person-title">VP, Sales MENA</p>

      <address class="address">
        2740 - 41 Street, Norvale,<br>
        Westmark, K4P 2J7 Zerhani Tower<br>
        Office No. 614-616, 6th Floor<br>
        Qasr Nadeem Road, Hessa<br>
        P.O. Box 4827, Dubai, UAE
      </address>

      <ul class="contacts">
        <li>
          <span class="contact-icon phone-icon">
            <svg viewBox="0 0 24 24" width="18" height="18" aria-hidden="true">
              <path fill="currentColor" d="M6.6 10.8a15.1 15.1 0 0 0 6.6 6.6l2.2-2.2a1 1 0 0 1 1-.25 11.4 11.4 0 0 0 3.6.57 1 1 0 0 1 1 1V20a1 1 0 0 1-1 1A17 17 0 0 1 3 4a1 1 0 0 1 1-1h3.5a1 1 0 0 1 1 1c0 1.25.2 2.45.57 3.6a1 1 0 0 1-.25 1z"/>
            </svg>
          </span>
          +971 508461270
        </li>
        <li>
          <span class="contact-icon">@</span>
          owen.pallister@korvexglb.example
        </li>
        <li>
          <span class="contact-icon web-icon">
            <svg viewBox="0 0 24 24" width="18" height="18" aria-hidden="true">
              <circle cx="12" cy="12" r="9.5" fill="none" stroke="currentColor" stroke-width="1.8"/>
              <ellipse cx="12" cy="12" rx="4" ry="9.5" fill="none" stroke="currentColor" stroke-width="1.5"/>
              <line x1="2.5" y1="12" x2="21.5" y2="12" stroke="currentColor" stroke-width="1.5"/>
            </svg>
          </span>
          www.korvexglb.example
        </li>
      </ul>
    </section>

    <div class="footer-band"></div>
  </article>
</body>
</html>
```